Multi-Faceted Legal and Finanacial Advisory Group Needs Business Card Design

We need a business card design for a newly branded Orlando Florida area advising group consisting of Attorneys, Accountants and Financial Planners. The company is named TK Counsel Partners. You will find our initial work on a business card. The information on the business card are merely guideposts and not final product. The logo does not have the be the same as provided since we have not finalized the logo. We would like to stay with a black/white/grey color scheme, but limited use of color is not out of the question.

Target Market(s)

Businesses and their Corporate Representatives

Industry/Entity Type

Business

Contact Information for Business Card

Should have Name, Title, Phone, Cell, Fax, Email and website. Logo should incorporate TK in some fashion however final logo used does not have to be the one on the document provided.

Requirements
Must have
• An TK design on front and back.

```html
<!DOCTYPE html>
<html lang="en">
<head>
<meta charset="utf-8">
<title>TK Counsel Partners – Business Card</title>
<link href="https://fonts.googleapis.com/css2?family=Tinos:wght@400;700&display=swap" rel="stylesheet">
<style>
  :root {
    --backdrop: #d9d9d9;
    --card-white: #ffffff;
    --ink: #111111;
    --panel-black: #0b0b0b;
    --panel-text: #f2f2f2;
    --shadow: rgba(0,0,0,0.18);
  }
  * { margin: 0; padding: 0; box-sizing: border-box; }
  html, body {
    width: 1200px; height: 897px; overflow: hidden;
    background: var(--backdrop);
    font-family: "Tinos", "Times New Roman", serif;
  }
  .sheet {
    width: 1200px; height: 897px;
    display: flex; flex-direction: column;
    align-items: center; justify-content: center; gap: 44px;
  }
  .card {
    width: 660px; height: 377px;
    background: var(--card-white);
    box-shadow: 0 6px 18px var(--shadow);
    position: relative; overflow: hidden;
  }
  /* Front */
  .card-front {
    display: flex; align-items: center; justify-content: center; gap: 22px;
  }
  .brand-square {
    width: 78px; height: 78px;
    border: 3px solid var(--ink);
    flex: none;
  }
  .brand-block { display: flex; flex-direction: column; align-items: center; }
  .brand-name {
    font-size: 42px; font-weight: 400; color: var(--ink); letter-spacing: 0.5px;
  }
  .brand-tagline {
    margin-top: 6px; font-size: 12px; color: var(--ink); letter-spacing: 0.5px;
  }
  /* Back */
  .card-back { display: flex; }
  .contact-panel {
    width: 56%; height: 100%;
    background: var(--panel-black); color: var(--panel-text);
    padding: 112px 0 0 52px;
    font-size: 17px; line-height: 1.32;
  }
  .contact-name { font-weight: 700; font-size: 19px; }
  .contact-title { font-style: italic; }
  .brand-panel {
    flex: 1; display: flex; flex-direction: column;
    align-items: center; justify-content: center; gap: 18px;
  }
  .brand-panel .brand-square { width: 96px; height: 96px; }
  .brand-panel .brand-name { font-size: 30px; text-align: center; line-height: 1.15; }
</style>
</head>
<body>
  <main class="sheet">
    <section class="card card-front">
      <div class="brand-square"></div>
      <div class="brand-block">
        <div class="brand-name">TK Counsel Partners</div>
        <div class="brand-tagline">Attorneys • Accountants • Financial Planners</div>
      </div>
    </section>

    <section class="card card-back">
      <div class="contact-panel">
        <div class="contact-name">Daniel R. Whitford, Esq.</div>
        <div class="contact-title">Attorney</div>
        <div>2200 Meridian Way, Suite 410</div>
        <div>Sanford, FL 32771</div>
        <div>Off: (407) XXX-XXXX</div>
        <div>Cell: (407) XXX-XXXX</div>
        <div>Email: dwhitford@tkcounsel.com</div>
        <div>Web: www.tkcounsel.com</div>
      </div>
      <div class="brand-panel">
        <div class="brand-square"></div>
        <div class="brand-name">TK Counsel<br>Partners</div>
      </div>
    </section>
  </main>
</body>
</html>
```